Party business requiring flyer and logo

Create a flyer (to be used online and offline) to promote a new business name for our business we are re-branding.
Business name
Marigold Fun and Games
Concept
# Birthday party room
# Parties that incorporate party room and full size basketball court
# Suitable for all ages, including adult parties
# Also available for hire by parent groups of young children to play
Facilities:
# General play space
# Full size basketball court
# Ball pit
# Portable soccer goal/reduced size basketball ring
# Movies
Catering and decorating packages available.
Private space, exclusive hire.
Catering to a large number of party themes.
Kitchen facilities available
Party host options
Note - we also require a new logo for this re-branding. We think about possibly keeping a similar look to the old logo with possibly replacing the A for a party hat etc. Happy to see whatever you come up with.
Existing business is called Harbourline Athletics, a basketball training and development facility. The new business needs to be linked to Harbourline Athletics from a banding perspective although does require its own identity
Brand essence - fun, vibrant, colourful, engaging
Industry/Entity Type
Entertainment
Logo Text
Marigold Fun and Games
Font styles to use
Colors
Designer to choose colors to be used in the design.
Requirements
Must have
- Must Have:
- - Must be vibrant, colourful and fun
- - Get across sense of energy
- - Our predominant market is children's parties however also needs to be relevant to adult parties also
Nice to have
- Contact details:
- Phone - 0472 916 253
- Email - lucyw@harbourlineathletics.com.au
- Web - www.marigoldfunandgames.com.au
Should not have
- Pricing
- Too specific details this will be a general flyer outlining briefly what we do without pigeon-holing us into a specific theme/category

```html
<!DOCTYPE html>
<html lang="en">
<head>
<meta charset="utf-8">
<title>Marigold Fun and Games – Party Venue Flyer</title>
<link rel="stylesheet" href="https://fonts.googleapis.com/css2?family=Andika:wght@700&family=Mali:wght@700&display=swap">
<style>
  :root {
    --purple: #8e2f93;
    --purple-dark: #7a2a86;
    --lime: #7fd63a;
    --canopy-purple: #8a2fd0;
    --wall: #f3b43a;
    --red: #e5322d;
    --yellow: #ffc21a;
    --pink: #ee2a8c;
    --badge-text: #ffd84a;
    --ink: #35284a;
    --blue: #2a3f9d;
    --sky: #2aa6e6;
    --orange: #f0793a;
    --cream: #fff6e6;
  }
  * { margin: 0; padding: 0; box-sizing: border-box; }
  html, body { width: 900px; height: 1200px; overflow: hidden; background: #ffffff; }
  .flyer {
    position: relative;
    width: 900px;
    height: 1200px;
    overflow: hidden;
    background: var(--yellow);
    font-family: "Andika", "Trebuchet MS", sans-serif;
    font-weight: 700;
  }
  .venue-photo {
    position: absolute;
    left: 0; top: 0;
    width: 900px; height: 680px;
    background:
      linear-gradient(180deg, transparent 0 80%, var(--red) 80% 100%),
      linear-gradient(160deg, var(--lime) 0 42%, var(--canopy-purple) 42% 55%, var(--wall) 55% 100%);
  }
  .headline {
    position: absolute;
    left: 62px; top: 30px;
    font-family: "Mali", "Trebuchet MS", sans-serif;
    font-weight: 700;
    font-size: 80px;
    line-height: 0.98;
    letter-spacing: -1px;
    color: var(--purple);
  }
  .feature-list {
    list-style: none;
    position: absolute;
    color: var(--ink);
    font-size: 21px;
    line-height: 1.2;
  }
  .feature-list li {
    position: relative;
    padding-left: 32px;
    margin-bottom: 12px;
  }
  .feature-list li::before {
    content: "";
    position: absolute;
    left: 0; top: 4px;
    width: 17px; height: 17px;
    border-radius: 50%;
    background: var(--purple);
  }
  .feature-list--top { left: 70px; top: 226px; width: 520px; }
  .feature-list--bottom { left: 560px; top: 866px; width: 310px; font-size: 21px; }
  .feature-list--bottom li { margin-bottom: 16px; }
  .book-badge {
    position: absolute;
    left: 694px; top: 120px;
    width: 176px; height: 176px;
    border-radius: 50%;
    background: var(--pink);
    color: var(--badge-text);
    display: flex; align-items: center; justify-content: center;
    text-align: center;
    font-size: 29px;
    line-height: 1.1;
  }
  .icon { position: absolute; }
  .icon--phone { left: 80px; top: 690px; }
  .call-block {
    position: absolute;
    left: 180px; top: 724px;
    color: var(--blue);
  }
  .call-block .label { font-size: 27px; padding-left: 40px; line-height: 1.2; }
  .call-block .number { font-size: 34px; letter-spacing: 1px; line-height: 1.2; }
  .brand-name {
    position: absolute;
    left: 70px; top: 860px;
    display: flex; align-items: center; gap: 16px;
    color: var(--purple);
    font-size: 44px;
    line-height: 1.05;
  }
  .brand-name .dot {
    flex: none;
    width: 34px; height: 34px;
    border-radius: 50%;
    background: var(--pink);
  }
  .icon--mail { left: 60px; top: 968px; }
  .icon--pin { left: 458px; top: 986px; }
  .contact-band {
    position: absolute;
    left: 0; top: 1050px;
    width: 900px; height: 150px;
    background: var(--purple-dark);
    color: var(--cream);
    font-size: 22px;
    line-height: 1.4;
  }
  .contact-band .web-mail { position: absolute; left: 40px; top: 34px; }
  .contact-band .address { position: absolute; left: 520px; top: 22px; font-style: normal; }
</style>
</head>
<body>
<main class="flyer">
  <div class="venue-photo" role="img" aria-label="Photo of the colourful party room with green and purple shade sails, fairy lights, yellow walls, red floor and bright silhouettes of children jumping"></div>

  <h1 class="headline">Your exclusive<br>Party Venue!</h1>

  <ul class="feature-list feature-list--top">
    <li>Catering and decorating packages available</li>
    <li>Private space, exclusive hire</li>
    <li>Catering to a large number of<br>party themes</li>
  </ul>

  <div class="book-badge">BOOK<br>ONLINE<br>NOW!</div>

  <svg class="icon icon--phone" width="74" height="118" viewBox="0 0 74 118" aria-hidden="true">
    <rect x="4" y="4" width="66" height="110" rx="10" fill="none" stroke="var(--purple)" stroke-width="5"/>
    <line x1="4" y1="22" x2="70" y2="22" stroke="var(--purple)" stroke-width="4"/>
    <line x1="4" y1="92" x2="70" y2="92" stroke="var(--purple)" stroke-width="4"/>
    <circle cx="37" cy="103" r="4" fill="var(--purple)"/>
  </svg>
  <div class="call-block">
    <div class="label">Call us on</div>
    <div class="number">0472 916 253</div>
  </div>

  <div class="brand-name"><span class="dot"></span><span>Marigold Fun<br>and Games</span></div>

  <ul class="feature-list feature-list--bottom">
    <li>Kitchen facilities<br>available</li>
    <li>Party host options</li>
    <li>Suitable for all ages,<br>including adult parties</li>
  </ul>

  <svg class="icon icon--mail" width="100" height="70" viewBox="0 0 100 70" aria-hidden="true">
    <rect x="4" y="4" width="92" height="62" rx="4" fill="none" stroke="var(--sky)" stroke-width="5"/>
    <polyline points="6,8 50,42 94,8" fill="none" stroke="var(--sky)" stroke-width="5" stroke-linejoin="round"/>
  </svg>
  <svg class="icon icon--pin" width="56" height="80" viewBox="0 0 56 80" aria-hidden="true">
    <path d="M28 78 C14 56 3 42 3 28 A25 25 0 0 1 53 28 C53 42 42 56 28 78 Z" fill="var(--orange)"/>
    <circle cx="28" cy="27" r="10" fill="none" stroke="var(--yellow)" stroke-width="5"/>
  </svg>

  <footer class="contact-band">
    <div class="web-mail">
      www.marigoldfunandgames.com.au<br>
      lucyw@harbourlineathletics.com.au
    </div>
    <address class="address">
      Unit 4, 22-24 Wattle Lane<br>
      Brookvale Heights, VIC<br>
      (Inside Harbourline Athletics)
    </address>
  </footer>
</main>
</body>
</html>
```